Website Design for Harbor 7340

We need a website design for a new company that strives to provide training and structure for religious missionaries who are traveling the world to teach of christianity.
They provide training in:
- Nutrition Coaching & Daily assignments
- Personal Training Sessions
- Phycological emotional/mental component
The goal of Harbor 7340 is to help missionaries preach the gospel of christ to those who haven't heard it due to geographical obstacles and physical limitations that get in the way.
The homepage template has linked images to use. If any other images are needed, stock images are acceptable.

Logo/Color Scheme: https://files.quorvex.net/share/8Kd2Lm9XpQ4rTz7WvN3bYc6HsJ1aFe0Gu

Customer Avatar/Core Message Canvas: https://sheets.plendora.net/s/4Rq81ZtyMn2wXcVb7KpLd0HsJ9aFgE3QuTo6YiPxNe/view

Homepage Template: https://docs.plendora.net/d/7Nw52KxpTr8vYzQm3LcBf1GhJ6dSeA0RuWo4XiZqPk/view

```html
<!DOCTYPE html>
<html lang="en">
<head>
<meta charset="utf-8">
<title>Harbor 7340 — Missionary Training</title>
<link href="https://fonts.googleapis.com/css2?family=Fira+Sans:wght@300;400;500;600&family=Lato:wght@400;700&display=swap" rel="stylesheet">
<style>
:root{
  --olive:#2c331f;
  --gold:#e0b93b;
  --mist:#e6e4e3;
  --cream:#fbf3dc;
  --ink:#2a2a2a;
  --white:#ffffff;
  --field:#e9e8e7;
}
*{margin:0;padding:0;box-sizing:border-box}
html,body{width:1200px;height:4154px;overflow:hidden}
body{font-family:"Lato",sans-serif;color:var(--ink);background:var(--white);position:relative}
.abs{position:absolute}
.heading{font-family:"Fira Sans",sans-serif;font-weight:500;letter-spacing:1.5px;text-align:center}
.btn{position:absolute;display:flex;align-items:center;justify-content:center;border-radius:20px;font-family:"Fira Sans",sans-serif;font-weight:600;font-size:13px;letter-spacing:.5px}
.btn-gold{background:var(--gold);color:var(--white);box-shadow:3px 3px 6px rgba(0,0,0,.25)}
.btn-dark{background:#111;color:var(--white)}

.site-header{position:absolute;top:0;left:0;width:1200px;height:71px;background:var(--white)}
.brand-name{font-family:"Fira Sans",sans-serif;font-weight:600;font-size:30px;color:var(--olive);line-height:1}
.site-header .brand-name{position:absolute;left:103px;top:20px}
.nav{position:absolute;top:26px;font-size:14px;color:#333}
.nav.active{color:var(--gold)}

.hero{position:absolute;top:71px;left:0;width:1200px;height:532px;background:linear-gradient(180deg,#0f3a1e 0%,#4a6b24 45%,#5a7a22 70%,#2a3a14 100%)}
.hero-title{position:absolute;left:102px;top:130px;font-family:"Fira Sans",sans-serif;font-weight:500;font-size:42px;line-height:48px;color:var(--white);letter-spacing:1px}
.hero-sub{position:absolute;left:102px;top:293px;width:640px;font-size:13px;line-height:21px;color:var(--white)}

.staff{position:absolute;top:603px;left:0;width:1200px;height:660px;background:var(--mist)}
.staff-card{position:absolute;width:200px;text-align:center}
.staff-card svg{display:block;margin:0 auto}
.staff-label{margin-top:20px;font-family:"Fira Sans",sans-serif;font-weight:500;font-size:15px;letter-spacing:1.5px;color:#222}

.barriers{position:absolute;top:1263px;left:0;width:1200px;height:615px;background:radial-gradient(ellipse at 50% 50%,#8a6c0c 0%,#6b5408 55%,#4d3c05 100%)}
.barriers p{position:absolute;text-align:center;color:var(--white)}

.approach{position:absolute;top:1878px;left:0;width:1200px;height:601px;background:var(--white)}
.pillar{position:absolute;width:300px;text-align:center}
.pillar h3{font-family:"Fira Sans",sans-serif;font-weight:500;font-size:22px;letter-spacing:1px;color:#2a2a2a;margin-top:14px}
.pillar p{font-size:14px;line-height:22px;color:#444;margin-top:12px}

.audience{position:absolute;top:2479px;left:0;width:1200px;height:692px;background:radial-gradient(ellipse at 50% 20%,#e9c860 0%,var(--gold) 55%,#d9b230 100%)}
.aud-card{position:absolute;top:160px;width:313px;height:401px;background:var(--cream)}
.aud-photo{width:313px;height:133px}
.aud-card h4{margin:24px 24px 0;font-family:"Fira Sans",sans-serif;font-weight:600;font-size:14px;letter-spacing:.5px;color:#222}
.aud-card p{margin:8px 24px 0;font-family:"Fira Sans",sans-serif;font-size:13px;line-height:21px;color:#333}

.newsletter{position:absolute;top:3171px;left:0;width:1200px;height:667px;background:var(--mist)}
.form-card{position:absolute;left:245px;top:204px;width:718px;height:410px;background:var(--white);border-radius:14px;box-shadow:0 2px 6px rgba(0,0,0,.08)}
.field{position:absolute;height:37px;background:var(--field);border-radius:19px;font-size:11px;color:#888;padding:13px 0 0 26px}

.site-footer{position:absolute;top:3838px;left:0;width:1200px;height:316px;background:var(--olive)}
.foot-logo{position:absolute;left:101px;top:2px;width:190px;height:145px;background:var(--white);display:flex;align-items:center;justify-content:center}
.foot-logo .brand-name{font-size:26px}
.foot-h{position:absolute;font-family:"Fira Sans",sans-serif;font-weight:600;font-size:15px;letter-spacing:.5px;color:var(--white)}
.foot-link{position:absolute;font-family:"Fira Sans",sans-serif;font-size:13px;letter-spacing:.5px;color:var(--white)}
.social{position:absolute;top:185px;width:26px;height:26px;border-radius:50%;background:var(--gold)}
.copyright{position:absolute;top:293px;width:1200px;text-align:center;font-family:"Fira Sans",sans-serif;font-size:11px;letter-spacing:.5px;color:var(--gold)}
</style>
</head>
<body>

<header class="site-header">
  <span class="brand-name">Harbor 7340</span>
  <span class="nav active" style="left:444px">Programs</span>
  <span class="nav" style="left:553px">Events</span>
  <span class="nav" style="left:640px">Online Store</span>
  <span class="nav" style="left:768px">About Us</span>
  <span class="nav" style="left:873px">Contact Us</span>
  <span class="btn" style="left:973px;top:18px;width:124px;height:34px;background:var(--gold);color:#fff">Sign up</span>
</header>

<section class="hero" role="img" aria-label="Snow-capped mountain range under a green overlay">
  <h1 class="hero-title">Empowing Change:<br>By Illuminating Lives<br>Unexposed to The Gospel’s Light</h1>
  <p class="hero-sub">Harbor 7340’s mission is to enable the word of Jesus to be experienced by people in the most remote and treacherous parts of the world</p>
  <span class="btn btn-gold" style="left:104px;top:370px;width:188px;height:32px">View Our Programs</span>
  <span class="btn btn-dark" style="left:310px;top:370px;width:187px;height:32px">Register for Training</span>
</section>

<section class="staff">
  <h2 class="heading abs" style="left:0;top:60px;width:1200px;font-size:40px;line-height:50px;color:var(--olive)">Harbor 7340’s Well Rounded Staff for<br>Specialized Training</h2>
  <div class="staff-card" style="left:94px;top:203px"><svg width="130" height="134" viewBox="0 0 130 134"><polygon points="38,6 92,6 124,38 124,92 92,124 38,124 6,92 6,38" fill="#fff"/><path d="M6,96 L38,128 L92,128 L124,96" fill="none" stroke="var(--gold)" stroke-width="8"/><rect x="40" y="38" width="50" height="54" rx="6" fill="var(--olive)" role="img" aria-label="Pastor icon"/></svg><div class="staff-label">Pastor</div></div>
  <div class="staff-card" style="left:360px;top:203px"><svg width="130" height="134" viewBox="0 0 130 134"><polygon points="38,6 92,6 124,38 124,92 92,124 38,124 6,92 6,38" fill="#fff"/><path d="M6,96 L38,128 L92,128 L124,96" fill="none" stroke="var(--gold)" stroke-width="8"/><rect x="40" y="38" width="50" height="54" rx="6" fill="var(--olive)" role="img" aria-label="Nutritionist icon"/></svg><div class="staff-label">Nutritionist</div></div>
  <div class="staff-card" style="left:626px;top:203px"><svg width="130" height="134" viewBox="0 0 130 134"><polygon points="38,6 92,6 124,38 124,92 92,124 38,124 6,92 6,38" fill="#fff"/><path d="M6,96 L38,128 L92,128 L124,96" fill="none" stroke="var(--gold)" stroke-width="8"/><rect x="40" y="38" width="50" height="54" rx="6" fill="var(--olive)" role="img" aria-label="Dietician icon"/></svg><div class="staff-label">Dietician</div></div>
  <div class="staff-card" style="left:893px;top:203px"><svg width="130" height="134" viewBox="0 0 130 134"><polygon points="38,6 92,6 124,38 124,92 92,124 38,124 6,92 6,38" fill="#fff"/><path d="M6,96 L38,128 L92,128 L124,96" fill="none" stroke="var(--gold)" stroke-width="8"/><rect x="40" y="38" width="50" height="54" rx="6" fill="var(--olive)" role="img" aria-label="Professional trainer icon"/></svg><div class="staff-label">Professional Trainer</div></div>
  <div class="staff-card" style="left:94px;top:417px"><svg width="130" height="134" viewBox="0 0 130 134"><polygon points="38,6 92,6 124,38 124,92 92,124 38,124 6,92 6,38" fill="#fff"/><path d="M6,96 L38,128 L92,128 L124,96" fill="none" stroke="var(--gold)" stroke-width="8"/><rect x="40" y="38" width="50" height="54" rx="6" fill="var(--olive)" role="img" aria-label="Former ranger icon"/></svg><div class="staff-label">Former Ranger</div></div>
  <div class="staff-card" style="left:360px;top:417px"><svg width="130" height="134" viewBox="0 0 130 134"><polygon points="38,6 92,6 124,38 124,92 92,124 38,124 6,92 6,38" fill="#fff"/><path d="M6,96 L38,128 L92,128 L124,96" fill="none" stroke="var(--gold)" stroke-width="8"/><rect x="40" y="38" width="50" height="54" rx="6" fill="var(--olive)" role="img" aria-label="Former special ops icon"/></svg><div class="staff-label">Former Special Ops</div></div>
  <div class="staff-card" style="left:626px;top:417px"><svg width="130" height="134" viewBox="0 0 130 134"><polygon points="38,6 92,6 124,38 124,92 92,124 38,124 6,92 6,38" fill="#fff"/><path d="M6,96 L38,128 L92,128 L124,96" fill="none" stroke="var(--gold)" stroke-width="8"/><rect x="40" y="38" width="50" height="54" rx="6" fill="var(--olive)" role="img" aria-label="Psychologist icon"/></svg><div class="staff-label">Psychologist</div></div>
  <div class="staff-card" style="left:893px;top:417px"><svg width="130" height="134" viewBox="0 0 130 134"><polygon points="38,6 92,6 124,38 124,92 92,124 38,124 6,92 6,38" fill="#fff"/><path d="M6,96 L38,128 L92,128 L124,96" fill="none" stroke="var(--gold)" stroke-width="8"/><rect x="40" y="38" width="50" height="54" rx="6" fill="var(--olive)" role="img" aria-label="Former special ops icon"/></svg><div class="staff-label">Former Special Ops</div></div>
</section>

<section class="barriers" role="img" aria-label="Golden textured backdrop with a faint world map">
  <h2 class="heading abs" style="left:0;top:55px;width:1200px;font-size:40px;color:var(--white)">Why Harbor 7340 is Breaking Barriers</h2>
  <p style="left:100px;top:130px;width:1000px;font-family:'Fira Sans',sans-serif;font-weight:600;font-size:15px;line-height:25px;letter-spacing:.8px">Geographical challenges make some communities difficult for missionaries to reach. The Harbor 7340 program is designed to remove the physical limitations that can hinder us from bringing the Gospel to places that seem physically impossible to reach. Harbor 7340 is founded on Romans 15:20. In his letter to the Romans, Paul requests funding to take the Gospel to Spain. In this letter, he writes:</p>
  <svg class="abs" style="left:548px;top:268px" width="44" height="68" viewBox="0 0 44 68"><rect x="19" y="0" width="6" height="68" fill="var(--gold)"/><rect x="2" y="18" width="40" height="6" fill="var(--gold)"/></svg>
  <p style="left:180px;top:330px;width:840px;font-size:15px;line-height:25px;letter-spacing:.8px">“[20] and thus I make it my ambition to preach the gospel, not where Christ has already been named, lest I build on someone else’s foundation, [21] but it is written, “those who have never been told of him will see, and those who have never heard will understand.”</p>
  <p style="left:0;top:430px;width:1200px;font-size:15px;letter-spacing:.8px">(Romans 15:20-21)</p>
  <span class="btn btn-dark" style="left:508px;top:492px;width:178px;height:31px;font-weight:400;font-size:14px;letter-spacing:1px">Join Our Mission</span>
</section>

<section class="approach">
  <h2 class="heading abs" style="left:0;top:52px;width:1200px;font-size:40px;color:var(--olive)">Harbor 7340 Missionary Training Approach</h2>
  <div class="heading abs" style="left:0;top:111px;width:1200px;font-size:22px;color:var(--olive)">Mind - Body - Spirit</div>
  <div class="pillar" style="left:108px;top:210px"><div role="img" aria-label="Mind icon" style="width:58px;height:66px;margin:0 auto;background:#e9a53a;border-radius:28px 28px 10px 10px"></div><h3>Mind</h3><p>Psychologically, we will prepare the mind through counseling, breathing techniques, and simulations in order to prepare for psychological challenges that come with being in the field.</p></div>
  <div class="pillar" style="left:448px;top:207px"><div role="img" aria-label="Body icon" style="width:42px;height:80px;margin:0 auto;background:#f0b940;border-radius:20px 20px 8px 8px"></div><h3 style="margin-top:11px">Body</h3><p>Physically, we will prepare the body to overcome any physical limitations through rigorous exercises and nutritional coaching geared specifically to the geographical area the missionary plans to go.</p></div>
  <div class="pillar" style="left:793px;top:210px"><div role="img" aria-label="Spirit icon" style="width:70px;height:78px;margin:0 auto;background:#e9b23a;border-radius:34px 34px 6px 6px"></div><h3>Spirit</h3><p>Spiritually, we will prepare the soul to overcome spiritual challenges that arise in different areas of the world. Our curriculum is designed to prepare missionaries with a firm base of theological principles</p></div>
  <span class="btn btn-gold" style="left:468px;top:506px;width:277px;height:32px">View our detailed training program</span>
</section>

<section class="audience" role="img" aria-label="Gold-tinted backdrop of people gathered in worship">
  <h2 class="heading abs" style="left:0;top:50px;width:1200px;font-size:40px;color:var(--white)">Who is Harbor 7340 For?</h2>
  <div class="aud-card" style="left:101px"><div class="aud-photo" role="img" aria-label="Photo of a team meeting around a table" style="background:linear-gradient(135deg,#7a6a5a,#c9b9a5)"></div><h4>Sending Agencies for Missionaries</h4><p>Are you looking to improve the training you’re offering your flock? We have designed a program to align our training with your goals to spread the Gospel to people and places where Jesus remains unnamed &amp; unknown. Our training helps turn your missionaries to resilient, well-trained men and women.</p></div>
  <div class="aud-card" style="left:443px"><div class="aud-photo" role="img" aria-label="Photo of a group studying the Bible together" style="background:linear-gradient(135deg,#dcdcdc,#5a6a8a)"></div><h4>Missionaries</h4><p>Are you independently seeking to develop your knowledge and skills independently? We are here to help! We can customize a training approach that fits your specific needs. Let us support your missionary journey to spread the Gospel to the most remote and treacherous areas in the world.</p></div>
  <div class="aud-card" style="left:786px"><div class="aud-photo" role="img" aria-label="Photo of hands holding a rosary" style="background:linear-gradient(135deg,#f2f2f2,#3a3a3a)"></div><h4>Christian-based training program<br>for ALL!</h4><p style="margin-top:4px">Are you looking to support the missionary community? Well we have a solution for you! We also offer a customized, personal-training approach for everyone. Even if you’re not preparing for a mission, joining one of our training programs will allow you to support our missionaries through your own physical fitness</p></div>
  <span class="btn" style="left:473px;top:604px;width:255px;height:34px;background:var(--olive);color:#fff;box-shadow:3px 3px 6px rgba(0,0,0,.25)">View our Training Options</span>
</section>

<section class="newsletter">
  <h2 class="abs" style="left:0;top:50px;width:1200px;text-align:center;font-family:'Fira Sans',sans-serif;font-weight:300;font-size:26px;line-height:32px;color:#333;letter-spacing:.5px">Join our Missionary Training: Stay up-to-date on our training<br>programs, missionary success stories, and new program info</h2>
  <p class="abs" style="left:0;top:134px;width:1200px;text-align:center;font-size:14px;line-height:22px;color:#444">Subscribe and help us in supporting our missionaries as they spread the Gospel to all<br>corners and areas of the world</p>
  <div class="form-card">
    <div class="field" style="left:89px;top:45px;width:257px">Name</div>
    <div class="field" style="left:374px;top:45px;width:256px">Last name</div>
    <div class="field" style="left:89px;top:112px;width:257px">Phone Number</div>
    <div class="field" style="left:374px;top:112px;width:256px">E Mail</div>
    <div class="field" style="left:89px;top:178px;width:541px;height:113px;border-radius:16px">Your Message Here...</div>
    <span class="btn btn-gold" style="left:265px;top:333px;width:223px;height:35px">Submit Here</span>
  </div>
</section>

<footer class="site-footer">
  <div class="foot-logo"><span class="brand-name">Harbor 7340</span></div>
  <span class="social" style="left:101px"></span>
  <span class="social" style="left:139px"></span>
  <span class="social" style="left:177px"></span>
  <span class="social" style="left:215px"></span>
  <span class="social" style="left:253px"></span>

  <div class="foot-h" style="left:535px;top:44px">Quick Links</div>
  <div class="foot-link" style="left:535px;top:78px">Programs</div>
  <div class="foot-link" style="left:535px;top:110px">Events</div>
  <div class="foot-link" style="left:535px;top:142px">Online Store</div>
  <div class="foot-link" style="left:535px;top:174px">About Us</div>
  <div class="foot-link" style="left:535px;top:206px">Contact Us</div>

  <div class="foot-h" style="left:795px;top:44px">Harbor 7340 Location</div>
  <svg class="abs" style="left:793px;top:81px" width="14" height="11" viewBox="0 0 14 11"><rect x="0.5" y="0.5" width="13" height="10" fill="none" stroke="var(--gold)"/><path d="M1,1 L7,6 L13,1" fill="none" stroke="var(--gold)"/></svg>
  <div class="foot-link" style="left:818px;top:78px">hello@harbor7340.org</div>
  <svg class="abs" style="left:794px;top:112px" width="9" height="14" viewBox="0 0 9 14"><rect x="0.5" y="0.5" width="8" height="13" rx="1.5" fill="none" stroke="var(--gold)"/></svg>
  <div class="foot-link" style="left:815px;top:110px">+(555) 014 27380</div>
  <svg class="abs" style="left:793px;top:144px" width="13" height="13" viewBox="0 0 13 13"><circle cx="6.5" cy="6.5" r="6" fill="none" stroke="var(--gold)"/><path d="M0.5,6.5 H12.5 M6.5,0.5 V12.5" stroke="var(--gold)"/></svg>
  <div class="foot-link" style="left:815px;top:142px">www.harbor7340.org</div>
  <svg class="abs" style="left:794px;top:175px" width="10" height="14" viewBox="0 0 10 14"><path d="M5,14 C1,8 0,6.5 0,5 A5,5 0 0 1 10,5 C10,6.5 9,8 5,14 Z" fill="var(--gold)"/><circle cx="5" cy="5" r="2" fill="var(--olive)"/></svg>
  <div class="foot-link" style="left:815px;top:174px">18 Lantern Row, Millbrook Road 4412,</div>

  <div class="copyright">Harbor 7340 © 2023 All rights reserved. Terms of use and Privacy Policy</div>
</footer>

</body>
</html>
```